Flyer Design Project

I need a 3.5x8.5 landscape flyer design for a carpet cleaning business in Ottawa, Ontario Canada, called 'Foxmere Bright Wash'.The flyer is a special for the holiday season, and exclusive to Barrhaven residents. The featured deals are: Two rooms and a hallway (up to 300 sq. ft.) for $79.
Pet stain treatment for 25% off.

Our strong selling features are our toxin free cleaning and very fast dry times. Please visit our webpage: www.foxmerebrightwash.ca additional info.

I am looking for something bold and clever, yet fun and light hearted.

Target Market(s)

35+ couples, 2.3 kids and pets. Above avg. income and education

Industry/Entity Type

Landscape

Requirements
Must have
• The only must haves are the featured deals, and our blue/green house logo and a January 31st 2013 expiry date.
Should not have
• Absolutely no pictures of any carpet cleaning equipment.

```html
<!DOCTYPE html>
<html lang="en">
<head>
<meta charset="utf-8">
<title>Foxmere Bright Wash – Holiday Flyer</title>
<link rel="stylesheet" href="https://fonts.googleapis.com/css2?family=Oswald:wght@500;700&family=PT+Sans:wght@400;700&family=Parisienne&display=swap">
<style>
  :root {
    --stage: #dcd8d2;
    --navy: #1b2738;
    --navy-deep: #121c29;
    --navy-light: #2b3a4f;
    --brand-blue: #2e3194;
    --brand-green: #2f9a3c;
    --alert-red: #e3202a;
    --white: #ffffff;
    --ink: #333333;
    --box-light: #f4f4f4;
    --box-mid: #d7d7d7;
    --box-edge: #8a8f96;
    --deal-blue: #2a2f8c;
    --photo-warm: #e6d6bb;
    --photo-pale: #f7f3ec;
  }
  * { margin: 0; padding: 0; box-sizing: border-box; }
  html, body { width: 1200px; height: 1006px; overflow: hidden; }
  body { background: var(--stage); position: relative; font-family: "PT Sans", sans-serif; }

  .card { position: absolute; width: 993px; height: 408px; overflow: hidden; }
  .card--front { left: 96px; top: 82px; background: var(--white); }
  .card--back {
    left: 95px; top: 527px;
    background: radial-gradient(ellipse at 30% 40%, var(--navy-light) 0%, var(--navy) 55%, var(--navy-deep) 100%);
  }

  .front__wave { position: absolute; inset: 0; }
  .front__photo {
    position: absolute; left: 520px; top: 92px; width: 390px; height: 262px;
    border-radius: 60px 60px 0 0;
    background:
      linear-gradient(180deg, rgba(255,255,255,0) 70%, var(--white) 100%),
      radial-gradient(ellipse at 50% 40%, var(--photo-warm) 0%, #efe4d2 45%, var(--photo-pale) 100%);
  }
  .front__contact-label {
    position: absolute; left: 44px; top: 26px; line-height: 1;
    font-family: "Oswald", sans-serif; font-weight: 700; font-size: 34px; color: var(--white);
    letter-spacing: 0.5px;
  }
  .front__phone {
    position: absolute; left: 42px; top: 70px;
    font-family: "Oswald", sans-serif; font-weight: 700; font-size: 56px; line-height: 1;
    color: var(--alert-red); letter-spacing: 1px;
  }
  .front__headline {
    position: absolute; right: 32px; top: 20px; line-height: 1.2;
    font-family: "Parisienne", cursive; font-size: 40px; color: var(--white);
  }

  .brand { position: absolute; display: flex; align-items: center; gap: 14px; }
  .brand__mark { width: 22px; height: 22px; background: var(--brand-green); flex: none; }
  .brand__name {
    font-family: "PT Sans", sans-serif; font-weight: 700; color: var(--brand-blue); line-height: 0.95;
  }
  .card--front .brand { left: 42px; top: 244px; }
  .card--front .brand__name { font-size: 54px; }
  .card--back .brand { left: 70px; top: 72px; }
  .card--back .brand__name { font-size: 62px; color: #4a4fd0; }
  .card--back .brand__mark { width: 26px; height: 26px; }

  .tagline { position: absolute; font-size: 17px; line-height: 1.2; }
  .card--front .tagline { left: 84px; top: 376px; color: var(--ink); }
  .card--back .tagline { left: 112px; top: 235px; color: var(--white); font-size: 20px; }

  .front__web {
    position: absolute; left: 708px; top: 366px; line-height: 1.2;
    font-size: 19px; color: var(--ink);
  }

  .payment { position: absolute; left: 148px; top: 330px; display: flex; gap: 14px; align-items: center; }
  .payment__badge { height: 40px; border-radius: 4px; }
  .payment__badge--a { width: 64px; background: #e58a2c; border-radius: 20px; }
  .payment__badge--b { width: 90px; background: #2a4fa0; }
  .payment__badge--c { width: 40px; background: #f2c21a; }

  .deals__title {
    position: absolute; left: 562px; width: 382px; top: 24px; text-align: center; line-height: 1.2;
    font-family: "Oswald", sans-serif; font-weight: 700; font-style: italic; font-size: 28px; color: var(--white);
  }
  .deal-box {
    position: absolute; left: 562px; width: 382px; border-radius: 9px;
    border: 2px solid var(--box-edge);
    background: linear-gradient(180deg, var(--box-light) 0%, #ececec 60%, var(--box-mid) 100%);
    text-align: center; color: var(--deal-blue);
  }
  .deal-box--offers { top: 76px; height: 131px; padding-top: 8px; }
  .deal-box--contact { top: 229px; height: 142px; padding-top: 12px; }
  .offer__main { font-family: "Oswald", sans-serif; font-weight: 500; font-size: 25px; line-height: 1.3; }
  .offer__price { font-size: 31px; font-weight: 700; }
  .offer__pet {
    margin-top: 8px; font-family: "Oswald", sans-serif; font-weight: 500; font-size: 20px; color: #333840;
  }
  .contact__line { font-family: "Oswald", sans-serif; font-weight: 700; color: var(--alert-red); line-height: 1.3; }
  .contact__label { font-size: 20px; }
  .contact__phone { font-size: 40px; letter-spacing: 0.5px; }
  .contact__web { font-size: 16px; color: var(--ink); margin-top: 4px; }
  .contact__expiry { font-size: 19px; font-weight: 700; margin-top: 12px; color: var(--deal-blue); }
</style>
</head>
<body>

<section class="card card--front" aria-label="Flyer front">
  <svg class="front__wave" width="993" height="408" viewBox="0 0 993 408" aria-hidden="true">
    <defs>
      <linearGradient id="navyFill" x1="0" y1="0" x2="0" y2="1">
        <stop offset="0" stop-color="#223147"/>
        <stop offset="1" stop-color="#17212f"/>
      </linearGradient>
    </defs>
    <path d="M0 0 H993 V262 C985 242 968 232 948 240 C930 247 920 235 910 215 C860 175 780 190 700 205
             C600 215 520 200 420 192 C360 186 310 178 270 178 C240 178 226 168 224 145
             C222 132 214 128 204 140 C180 168 150 176 100 168 C60 160 30 155 0 170 Z" fill="url(#navyFill)"/>
  </svg>
  <div class="front__photo" role="img" aria-label="Photo of a parent and toddler reading a book together on a soft white carpet"></div>

  <p class="front__contact-label">Contact us:</p>
  <p class="front__phone">613-555-0142</p>
  <p class="front__headline">Barrhaven Exclusive Deal</p>

  <div class="brand">
    <span class="brand__mark" aria-hidden="true"></span>
    <p class="brand__name">Foxmere<br>Bright Wash</p>
  </div>
  <p class="tagline">Cleaner carpets...healthier homes</p>

  <p class="front__web">www.foxmerebrightwash.ca</p>
</section>

<section class="card card--back" aria-label="Flyer back">
  <div class="brand">
    <span class="brand__mark" aria-hidden="true"></span>
    <p class="brand__name">Foxmere<br>Bright Wash</p>
  </div>
  <p class="tagline">Cleaner carpets...healthier homes</p>

  <div class="payment" aria-label="Accepted payment methods">
    <span class="payment__badge payment__badge--a"></span>
    <span class="payment__badge payment__badge--b"></span>
    <span class="payment__badge payment__badge--c"></span>
  </div>

  <p class="deals__title">Featured deals</p>
  <div class="deal-box deal-box--offers">
    <p class="offer__main">Two rooms and a hallway<br>(Up to 300 sq. ft.) <span class="offer__price">for $79</span></p>
    <p class="offer__pet">PET STAIN TREATMENT FOR 25% OFF</p>
  </div>
  <div class="deal-box deal-box--contact">
    <p class="contact__line"><span class="contact__label">Contact us:</span> <span class="contact__phone">613-555-0142</span></p>
    <p class="contact__web">www.foxmerebrightwash.ca</p>
    <p class="contact__expiry">Expiry date: January 31st 2013</p>
  </div>
</section>

</body>
</html>
```